Moulding supply company needs a Door Hanger Design

Door Hanger Design Request from Ledge Craft
www. ledgecrafts.example
We are moulding factory outlet in Toronto. Provide high quality moulding materials with competitive price like crown mouldings, casings, wainscoting, flatstocks, baseboards. We also provide professional installation for our clients. This door hanger will help the home owner easily find a local factory supplier with providing the materials as well as installation.

Detail request for design:
Size: 4”x11”, vertical
Shape: Rectangle

Content:
Front
1. Logo, see attachment(Use the left one, horizontal one)
2. Moulding factory outlet direct sale
3. Supply high quality Crown mouldings, baseboards, casings and wainscotings with competitive price
4. Installation & delivery
#2 content is the most important content, should be bold and readable
#3 can be smaller font compare to #2

Address: 47 North Willow Vale Rd, Richmond Hill, ON L4B 3K9
Telephone: 416 555 0143
416 555 0187
Email: info@ledgecrafts.example

Back
Slogan: Convert plain room into designer’s interiors

Telephone: 416 555 0143
416 555 0187
Email: info@ledgecrafts.example

Images:
Front
1. Display our productions for crown mouldings, baseboards, casings and wainscotings, refer to our website www.ledgecrafts.example. (The winner finally we will provide the high resolution images, low resolution please copy from our website so far)
Back
2. Display 4-6 nice images for 1. wainscoting walls 2. feature walls, 3. waffle ceiling like attached below. BUT PLEASE DON'T USE THE IMAGES PROVIDED, THIS IS ONLY A SAMPLE. Please use high resolution images for printing. ALSO PLEASE DON'T LIMIT YOUR CREATIVITY TO USE 4 SQUARES LIKE BELOW IMAGES. Please provide more ideas

Note:
1. Please do the bleeding for final printing production
2. Images have to be high resolution for ready to print
3. Style need to be fresh, clean, easy to read, modern and magazine style
4. Information has to be readable, easy to find, front and back both need to display company address, telephone, email, you can use icon or abbreviation to do these information.

Thanks,
Ledge Crafts

```html
<!DOCTYPE html>
<html lang="en">
<head>
<meta charset="utf-8">
<title>Ledge Crafts Door Hangers</title>
<link rel="stylesheet" href="https://fonts.googleapis.com/css2?family=Open+Sans:ital,wght@0,400;0,600;0,700;1,700;1,800&family=Oswald:wght@600;700&display=swap">
<style>
  :root {
    --page: #ffffff;
    --night: #262932;
    --night-deep: #17191f;
    --slate: #3b3f4a;
    --snow: #ffffff;
    --mist: #e4e4e6;
    --ink-grey: #5f6268;
    --soft-grey: #9a9ca1;
    --orange: #e8501e;
    --royal: #1f4396;
    --photo-dark: #3a3029;
    --photo-mid: #5a4b40;
    --photo-light: #c9c6c2;
  }
  html, body {
    margin: 0;
    padding: 0;
    width: 1104px;
    height: 1200px;
    overflow: hidden;
    background: var(--page);
  }
  .canvas {
    position: relative;
    width: 1104px;
    height: 1200px;
  }
  .hanger {
    position: absolute;
    top: 67px;
    width: 372px;
    height: 1023px;
  }
  .hanger--back { left: 138px; }
  .hanger--front { left: 634px; }
  .hanger svg { display: block; width: 100%; height: 100%; }
  .brand-name { font-family: "Open Sans", sans-serif; font-weight: 600; font-size: 56px; letter-spacing: 2px; }
  .brand-tagline { font-family: "Open Sans", sans-serif; font-weight: 400; font-size: 16px; letter-spacing: 5px; }
  .slogan { font-family: "Open Sans", sans-serif; font-weight: 700; font-size: 40px; fill: var(--snow); }
  .card-title { font-family: "Oswald", sans-serif; font-weight: 600; font-size: 12.5px; fill: #3a3a3a; letter-spacing: .5px; }
  .card-size { font-family: "Open Sans", sans-serif; font-size: 10px; fill: #555; }
  .contact { font-family: "Open Sans", sans-serif; font-weight: 400; font-size: 18px; }
  .contact--dark { fill: var(--snow); }
  .contact--light { fill: var(--ink-grey); }
  .banner-text { font-family: "Oswald", sans-serif; font-weight: 700; fill: var(--snow); }
  .offer { font-family: "Open Sans", sans-serif; font-weight: 800; font-style: italic; font-size: 30px; fill: var(--orange); }
  .icon-ring { fill: none; stroke: var(--orange); stroke-width: 3; }
  .icon-glyph { fill: none; stroke: var(--orange); stroke-width: 2.6; stroke-linecap: round; stroke-linejoin: round; }
</style>
</head>
<body>
<main class="canvas">

  <!-- Back side -->
  <section class="hanger hanger--back">
    <svg viewBox="0 0 600 1650" xmlns="http://www.w3.org/2000/svg">
      <defs>
        <linearGradient id="nightFill" x1="0" y1="0" x2="1" y2="1">
          <stop offset="0" stop-color="var(--night-deep)"/>
          <stop offset=".5" stop-color="var(--slate)"/>
          <stop offset="1" stop-color="var(--night-deep)"/>
        </linearGradient>
        <linearGradient id="roomFill" x1="0" y1="0" x2="1" y2="0">
          <stop offset="0" stop-color="var(--photo-light)"/>
          <stop offset=".25" stop-color="var(--photo-mid)"/>
          <stop offset="1" stop-color="var(--photo-dark)"/>
        </linearGradient>
        <clipPath id="backShape">
          <path d="M0,300 A300,300 0 0 1 600,300 L600,1600 Q600,1650 550,1650 L50,1650 Q0,1650 0,1600 L0,570 Q0,520 50,520 L300,520 A175,175 0 1 0 125,345 L125,322 Q125,362 85,362 L40,362 Q0,362 0,322 Z"/>
        </clipPath>
      </defs>
      <g clip-path="url(#backShape)">
        <rect class="hanger-base" width="600" height="1650" fill="url(#nightFill)"/>
        <path class="room-photo" role="img" aria-label="Photo of a dining room with dark panelled wainscoting walls and a textured white vase"
              d="M0,742 H600 V1392 Q600,1432 560,1432 H40 Q0,1432 0,1392 Z" fill="url(#roomFill)"/>
      </g>

      <g class="brand">
        <rect x="58" y="582" width="22" height="22" fill="var(--soft-grey)"/>
        <text class="brand-name" x="160" y="625" fill="var(--ink-grey)">Ledge Crafts</text>
        <text class="brand-tagline" x="166" y="662" fill="var(--ink-grey)">FOR ALL TYPES OF PROJECTS</text>
      </g>

      <g class="slogan-block">
        <path d="M36,790 V772 H100" fill="none" stroke="var(--soft-grey)" stroke-width="10"/>
        <text class="slogan" x="55" y="825">Convert plain room into</text>
        <text class="slogan" x="55" y="868">designer’s interiors</text>
        <path d="M415,885 H450 V852" fill="none" stroke="var(--orange)" stroke-width="6"/>
      </g>

      <g class="product-cards">
        <g class="product-card">
          <rect x="191" y="955" width="162" height="162" rx="14" fill="var(--snow)" stroke="var(--orange)" stroke-width="2"/>
          <rect x="232" y="968" width="80" height="78" rx="6" fill="var(--mist)" role="img" aria-label="Chair rail moulding profile"/>
          <text class="card-title" x="214" y="1076">COLONIAL CHAIR RAIL</text>
          <text class="card-size" x="214" y="1092">3 1/4 x 1" x 16</text>
        </g>
        <g class="product-card">
          <rect x="370" y="977" width="162" height="162" rx="14" fill="var(--snow)" stroke="var(--orange)" stroke-width="2"/>
          <rect x="411" y="990" width="80" height="78" rx="6" fill="var(--mist)" role="img" aria-label="Chair rail moulding profile"/>
          <text class="card-title" x="393" y="1098">COLONIAL CHAIR RAIL</text>
          <text class="card-size" x="393" y="1114">3 1/4 x 1" x 16</text>
        </g>
        <g class="product-card">
          <rect x="191" y="1139" width="162" height="162" rx="14" fill="var(--snow)" stroke="var(--orange)" stroke-width="2"/>
          <rect x="232" y="1152" width="80" height="78" rx="6" fill="var(--mist)" role="img" aria-label="Chair rail moulding profile"/>
          <text class="card-title" x="214" y="1260">COLONIAL CHAIR RAIL</text>
          <text class="card-size" x="214" y="1276">3 1/4 x 1" x 16</text>
        </g>
        <g class="product-card">
          <rect x="370" y="1157" width="162" height="162" rx="14" fill="var(--snow)" stroke="var(--orange)" stroke-width="2"/>
          <rect x="411" y="1170" width="80" height="78" rx="6" fill="var(--mist)" role="img" aria-label="Chair rail moulding profile"/>
          <text class="card-title" x="393" y="1278">COLONIAL CHAIR RAIL</text>
          <text class="card-size" x="393" y="1294">3 1/4 x 1" x 16</text>
        </g>
      </g>

      <g class="contact-block">
        <circle class="icon-ring" cx="56" cy="1500" r="18"/>
        <path class="icon-glyph" d="M56,1512 C48,1502 48,1498 48,1495 A8,8 0 0 1 64,1495 C64,1498 64,1502 56,1512 Z"/>
        <text class="contact contact--dark" x="82" y="1506">47 North Willow Vale Rd,</text>
        <text class="contact contact--dark" x="82" y="1533">Richmond Hill, ON L4B 3K9</text>

        <circle class="icon-ring" cx="370" cy="1500" r="18"/>
        <path class="icon-glyph" d="M361,1494 H379 V1507 H361 Z M361,1494 L370,1502 L379,1494"/>
        <text class="contact contact--dark" x="395" y="1506" style="font-size:16px">info@ledgecrafts.example</text>

        <circle class="icon-ring" cx="56" cy="1568" r="18"/>
        <path class="icon-glyph" d="M49,1559 Q46,1562 48,1567 Q52,1575 60,1578 Q64,1579 66,1576 L62,1572 L59,1574 Q54,1571 52,1565 L54,1562 Z"/>
        <text class="contact contact--dark" x="82" y="1574">416 555 0143/416 555 0187</text>

        <circle class="icon-ring" cx="370" cy="1568" r="18"/>
        <circle class="icon-glyph" cx="370" cy="1568" r="10"/>
        <path class="icon-glyph" d="M360,1568 H380 M370,1558 V1578 M362,1562 H378 M362,1574 H378" stroke-width="1.6"/>
        <text class="contact contact--dark" x="395" y="1574" style="font-size:16px">www.ledgecrafts.example</text>
      </g>
    </svg>
  </section>

  <!-- Front side -->
  <section class="hanger hanger--front">
    <svg viewBox="0 0 600 1650" xmlns="http://www.w3.org/2000/svg">
      <defs>
        <linearGradient id="snowFill" x1="0" y1="0" x2="1" y2="1">
          <stop offset="0" stop-color="#f4f4f5"/>
          <stop offset=".5" stop-color="#ffffff"/>
          <stop offset="1" stop-color="#e9e9eb"/>
        </linearGradient>
      </defs>
      <path class="hanger-base" d="M0,300 A300,300 0 0 1 600,300 L600,1600 Q600,1650 550,1650 L50,1650 Q0,1650 0,1600 L0,570 Q0,520 50,520 L300,520 A175,175 0 1 0 125,345 L125,322 Q125,362 85,362 L40,362 Q0,362 0,322 Z"
            fill="url(#snowFill)" stroke="#3a3a3a" stroke-width="1.2"/>

      <g class="brand">
        <rect x="82" y="582" width="22" height="22" fill="var(--soft-grey)"/>
        <text class="brand-name" x="180" y="625" fill="var(--ink-grey)">Ledge Crafts</text>
        <text class="brand-tagline" x="190" y="662" fill="var(--ink-grey)">FOR ALL TYPES OF PROJECTS</text>
      </g>

      <g class="headline-banners">
        <polygon points="108,732 503,685 503,877 98,924 130,830" fill="var(--royal)"/>
        <polygon points="108,932 503,884 503,1017 98,1062 125,990" fill="var(--orange)"/>
        <polygon points="130,1072 498,1029 473,1110 490,1160 130,1202" fill="var(--royal)"/>
        <text class="banner-text" transform="translate(155,815) rotate(-6.8)" font-size="100" textLength="320">MOULDING</text>
        <text class="banner-text" transform="translate(178,895) rotate(-6.8)" font-size="96" textLength="270">FACTORY</text>
        <text class="banner-text" transform="translate(158,1035) rotate(-6.8)" font-size="124" textLength="295">OUTLET</text>
        <text class="banner-text" transform="translate(152,1160) rotate(-6.8)" font-size="72" textLength="297">DIRECT SALE</text>
      </g>

      <g class="offer-block">
        <path d="M50,1240 V1218 H115" fill="none" stroke="var(--soft-grey)" stroke-width="10"/>
        <text class="offer" x="72" y="1265">Supply high quality Crown</text>
        <text class="offer" x="72" y="1302">mouldings, baseboards, casings</text>
        <text class="offer" x="72" y="1339">and wainscotings with</text>
        <text class="offer" x="72" y="1376">competitive price</text>
        <text class="offer" x="72" y="1413">Installation &amp; delivery</text>
        <path d="M380,1433 H415 V1405" fill="none" stroke="var(--soft-grey)" stroke-width="8"/>
      </g>

      <g class="contact-block">
        <circle class="icon-ring" cx="60" cy="1500" r="18"/>
        <path class="icon-glyph" d="M60,1512 C52,1502 52,1498 52,1495 A8,8 0 0 1 68,1495 C68,1498 68,1502 60,1512 Z"/>
        <text class="contact contact--light" x="86" y="1506">47 North Willow Vale Rd,</text>
        <text class="contact contact--light" x="86" y="1533">Richmond Hill, ON L4B 3K9</text>

        <circle class="icon-ring" cx="374" cy="1500" r="18"/>
        <path class="icon-glyph" d="M365,1494 H383 V1507 H365 Z M365,1494 L374,1502 L383,1494"/>
        <text class="contact contact--light" x="399" y="1506" style="font-size:16px">info@ledgecrafts.example</text>

        <circle class="icon-ring" cx="60" cy="1568" r="18"/>
        <path class="icon-glyph" d="M53,1559 Q50,1562 52,1567 Q56,1575 64,1578 Q68,1579 70,1576 L66,1572 L63,1574 Q58,1571 56,1565 L58,1562 Z"/>
        <text class="contact contact--light" x="86" y="1574">416 555 0143/416 555 0187</text>

        <circle class="icon-ring" cx="374" cy="1568" r="18"/>
        <circle class="icon-glyph" cx="374" cy="1568" r="10"/>
        <path class="icon-glyph" d="M364,1568 H384 M374,1558 V1578 M366,1562 H382 M366,1574 H382" stroke-width="1.6"/>
        <text class="contact contact--light" x="399" y="1574" style="font-size:16px">www.ledgecrafts.example</text>
      </g>
    </svg>
  </section>

</main>
</body>
</html>
```